Postcard Design

We need a postcard designed for our company Clastor-Ox. Clastor-ox specializes in providing a tailored document destruction service that allows businesses to comply with legislation and ensure that the client, employee and confidential business information is kept secure at all times. We would like to see a postcard with greys, blues, blacks, and whites in it. I have attached a few logos for your reference. I would like the front of the postcard to be a picture design only with our company logo info. The back should have a message that says:

Dear Valued Customer,
We are sending you this letter because you currently utilize our On-site paper destruction service. We want to make you aware of our Plant-Based paper destruction service and the benefits to you and to the environment. Currently, 60% of our customers receive, and are highly satisfied with our Plant-Based Service.

Definitions:
On-site Service – Customer’s material is destroyed at the Customer’s location
Plant-Based Service – Customer’s material is destroyed at a Clastor-ox Secured Facility

What Would Not Change:

Security:
- All trucks are equipped with GPS tracking devices
- Our facility is monitored by CCTV 24 hours a day 7 days a week
- Our box trucks are equipped with secure alarm systems
- Annual Background Checks and Drug Screens are ran on all employees

Plant-Based Service Benefits:
- Less Noise at your Location
- Less Time in your Parking Lot
- Reduced Fuel Consumption
- Environmentally Friendly
- Flexibility
- Quicker turn-around times on all Service Requests (i.e., Purges / Earlier Pick-Ups)

We will begin changing your service from On-site to Plant Based starting August 1st. The process will take an additional 60 days to fully implement so you may not see a change right away. Our On-site capabilities are NOT going away. If you wish to remain an On-site customer all you have to do is call or email me your request. I am also available should you have any questions. My contact information is below.
We appreciate your consideration in regards to this matter and, as always, thank you for your business.

Martin L. Pruett
General Manager
Martin.Pruett@clastorox-mail.com
472.618.5037

is there enough room to get this on the back of the card?

Industry/Entity Type

It Company

```html
<!DOCTYPE html>
<html lang="en">
<head>
<meta charset="utf-8">
<title>Clastor-Ox Postcard Back</title>
<link href="https://fonts.googleapis.com/css2?family=Arimo:ital,wght@0,400;0,700;1,700&display=swap" rel="stylesheet">
<style>
  :root {
    --brand-blue: #2f73b8;
    --brand-blue-edge: #5b93cc;
    --heading-blue: #2e75bc;
    --ink: #262626;
    --ink-soft: #3a3a3a;
    --paper: #ffffff;
    --mist: #e9ebee;
    --logo-blue: #2d4f93;
  }
  * { margin: 0; padding: 0; box-sizing: border-box; }
  html, body { width: 1200px; height: 778px; overflow: hidden; background: var(--paper); }
  body { font-family: "Arimo", Arial, sans-serif; color: var(--ink); position: relative; }

  .card-back {
    position: absolute; left: 0; top: 0; width: 708px; height: 778px;
    background: linear-gradient(160deg, var(--mist) 0%, #f6f7f8 45%, var(--paper) 80%);
  }

  .greeting {
    position: absolute; left: 0; top: 0; width: 708px; height: 196px;
    background: var(--brand-blue);
    border-right: 1px solid var(--brand-blue-edge);
    border-bottom: 1px solid var(--brand-blue-edge);
    color: var(--paper);
    padding: 42px 21px 0 29px;
  }
  .greeting h1 { font-size: 21.5px; font-weight: 700; line-height: 26px; letter-spacing: -0.2px; }
  .greeting p { font-size: 16.8px; line-height: 24.4px; text-align: justify; letter-spacing: -0.1px; }

  .column { position: absolute; top: 220px; font-size: 16.4px; line-height: 19.6px; color: var(--ink); }
  .column-left { left: 28px; width: 340px; }
  .column-right { left: 403px; width: 290px; }

  .section-title { color: var(--heading-blue); font-size: 18.3px; font-weight: 700; line-height: 22px; }
  .definition { margin-bottom: 5px; }
  .definition em { font-weight: 700; font-style: italic; }
  .sub-title { font-weight: 700; color: var(--ink); }
  .what-stays { margin-top: 23px; }
  .benefits-title { margin-top: 18px; }

  .bullets { list-style: none; }
  .bullets li { position: relative; padding-left: 29px; }
  .bullets li::before {
    content: ""; position: absolute; left: 3px; top: 7px;
    width: 7px; height: 7px; border-radius: 50%; background: var(--ink-soft);
  }

  .column-right p { margin-bottom: 8px; }
  .signature { line-height: 19.2px; }
  .signature strong { display: block; }

  .brand-mark {
    position: absolute; left: 416px; top: 684px;
    display: flex; align-items: center; gap: 10px;
    font-size: 30px; font-weight: 700; color: var(--logo-blue); letter-spacing: -0.5px;
  }
  .brand-mark .square { width: 22px; height: 22px; background: var(--logo-blue); }
</style>
</head>
<body>
  <section class="card-back">
    <header class="greeting">
      <h1>Dear Valued Customer,</h1>
      <p>We are sending you this letter because you currently utilize our On-site paper destruction service. We want to make you aware of our Plant-Based paper destruction service and the benefits to you and to the environment. Currently, 60% of our customers receive, and are highly satisfied with our Plant-Based Service.</p>
    </header>

    <div class="column column-left">
      <h2 class="section-title">Definitions:</h2>
      <p class="definition"><em>On-site Service</em> – Customer’s material is destroyed at the Customer’s location</p>
      <p class="definition"><em>Plant-Based Service</em> – Customer’s material is destroyed at a Clastor-ox Secured Facility</p>

      <h2 class="section-title what-stays">What Would Not Change:</h2>
      <p class="sub-title">Security:</p>
      <ul class="bullets">
        <li>All trucks are equipped with GPS tracking devices</li>
        <li>Our facility is monitored by CCTV 24 hours a day 7 days a week. Our box trucks are equipped with secure alarm systems</li>
        <li>Annual Background Checks and Drug Screens are ran on all employees</li>
      </ul>

      <p class="sub-title benefits-title">Plant-Based Service Benefits:</p>
      <ul class="bullets">
        <li>Less Noise at your Location</li>
        <li>Less Time in your Parking Lot</li>
        <li>Reduced Fuel Consumption</li>
        <li>Environmentally Friendly</li>
        <li>Flexibility</li>
        <li>Quicker turn-around times on all Service Requests (i.e., Purges / Earlier Pick-Ups)</li>
      </ul>
    </div>

    <div class="column column-right">
      <p>We will begin changing your service from On-site to Plant Based starting August 1st. The process will take an additional 60 days to fully implement so you may not see a change right away. Our On-site capabilities are NOT going away. If you wish to remain an On-site customer all you have to do is call or email me your request. I am also available should you have any questions. My contact information is below.</p>
      <p>We appreciate your consideration in regards to this matter and, as always, thank you for your business.</p>
      <p class="signature">
        <strong>Martin L. Pruett</strong>
        General Manager<br>
        Martin.Pruett@clastorox-mail.com<br>
        472.618.5037
      </p>
    </div>

    <div class="brand-mark">
      <span class="square"></span>
      <span class="brand-name">Clastor-ox</span>
    </div>
  </section>
</body>
</html>
```